PowerPoint Template for our Business

We are looking for a professional and visually appealing PowerPoint template for our business, Pellion Labs. We specialize in calibration services and are currently undergoing a rebranding process. The new template should align with our updated brand identity, using the provided color palette and logos.
Project Requirements:
Title Slide:
Full Pellion Labs logo prominently displayed.
Clean and professional layout.
Background color should be white with brand accents.
Title and subtitle areas clearly defined.
Content Slide:
Consistent use of brand colors for headers, footers, and other elements.
Space for text, images, charts, and graphs.
PX logo subtly incorporated.
Clean and modern layout ensuring readability and professionalism.
Section Header Slide:
Clear differentiation from content slides.
Use of PX logo and brand color for background.
Professional typography.
Closing Slide:
Full Pellion Labs logo with a final message.
Clean background, professional layout.
Space for a thank you message and contact information.
Brand Colors:
Green: RGB (207, 255, 0)
Light Gray: RGB (239, 239, 239)
Gray: RGB (191, 191, 191)
Black: RGB (0, 0, 0)
White: RGB (255, 255, 255)
Deliverables:
A fully editable PowerPoint template (.pptx format).
Fonts and any additional assets used in the design.
Additional Information:
Please refer to the attached logos and color palette for guidance.
We are looking for a design that is not only professional and visually appealing but also functional for business presentations.
We look forward to seeing your creative proposals and selecting a design that best represents our brand.
Thank you!

```html
<!DOCTYPE html>
<html lang="en">
<head>
<meta charset="utf-8">
<title>Pellion Labs — Presentation Template</title>
<link rel="stylesheet" href="https://fonts.googleapis.com/css2?family=Poppins:wght@400;500;600;700;800&display=swap">
<style>
:root{
  --green:#cfff00;
  --light:#efefef;
  --gray:#bfbfbf;
  --black:#000;
  --white:#fff;
  --muted:#8c8c8c;
  --canvas:#d9dadd;
  --photo-a:#c9d6e2;
  --photo-b:#8ea4b8;
}
*{margin:0;padding:0;box-sizing:border-box}
html,body{width:1051px;height:1200px;overflow:hidden}
body{background:linear-gradient(160deg,#e3e4e7,var(--canvas));font-family:"Poppins",sans-serif;color:var(--black);position:relative}
.slide{position:absolute;width:321px;height:180px;background:var(--white);overflow:hidden;box-shadow:1px 2px 4px rgba(0,0,0,.2)}
.a{position:absolute}
.title{position:absolute;left:11px;top:10px;font-size:10.5px;font-weight:600;line-height:1.2}
.rule{position:absolute;width:11px;height:1.5px;background:var(--green)}
.brand{position:absolute;top:8px;right:7px;display:flex;align-items:center;gap:2px;font-size:4.6px;font-weight:500}
.brand i{display:block;width:7px;height:7px;background:var(--black)}
.pnum{position:absolute;left:6px;bottom:5px;font-size:3.4px}
.footline{position:absolute;left:12px;right:0;bottom:8px;height:.5px;background:var(--green)}
.tiny{font-size:2.8px;line-height:1.5;color:var(--muted)}
.tiny.w{color:var(--white)}
.bold{font-weight:600;color:var(--black)}
.photo{position:absolute;background:linear-gradient(140deg,var(--photo-a),var(--photo-b))}
.sq{position:absolute;background:var(--green)}
.num{position:absolute;width:11px;height:11px;background:var(--green);font-size:5.5px;font-weight:700;display:flex;align-items:center;justify-content:center}
.logo{position:absolute;display:flex;align-items:center;gap:5px;font-weight:500}
.logo i{display:block;background:var(--black)}
.item-h{font-size:6px;font-weight:600}
svg{position:absolute;left:0;top:0;overflow:visible}
</style>
</head>
<body>

<!-- Row 1 -->
<section class="slide" style="left:34px;top:32px">
  <div class="sq" style="left:7px;top:7px;width:7px;height:7px"></div>
  <div class="sq" style="left:202px;top:0;width:119px;height:13px"></div>
  <div class="sq" style="left:308px;top:0;width:13px;height:93px"></div>
  <div class="a" style="left:127px;top:158px;width:194px;height:22px;background:var(--gray)"></div>
  <div class="photo" role="img" aria-label="Scientist in a lab coat using a microscope" style="left:162px;top:18px;width:141px;height:146px"></div>
  <div class="logo" style="left:21px;top:35px;font-size:10px"><i style="width:22px;height:22px"></i>Pellion Labs</div>
  <div class="a" style="left:23px;top:89px;font-size:7.5px">Presentation</div>
  <div class="a" style="left:22px;top:96px;font-size:18px;font-weight:800;line-height:1.1">Business</div>
  <div class="a" style="left:23px;top:117px;font-size:13px;font-weight:600">Marketing</div>
  <div class="a" style="left:23px;top:160px;font-size:5.5px;letter-spacing:1.6px">www.pellionlabs.com</div>
</section>

<section class="slide" style="left:365px;top:32px">
  <div class="a" style="left:7px;top:7px;width:6px;height:6px;background:var(--gray)"></div>
  <div class="photo" role="img" aria-label="Researcher looking into a microscope" style="left:135px;top:0;width:186px;height:153px"></div>
  <div class="sq" style="left:135px;top:153px;width:186px;height:27px"></div>
  <div class="a" style="left:135px;top:163px;width:186px;text-align:center;font-size:5.5px;letter-spacing:1.6px">www.pellionlabs.com</div>
  <div class="logo" style="left:20px;top:29px;font-size:10px"><i style="width:21px;height:21px"></i>Pellion Labs</div>
  <div class="a" style="left:20px;top:95px;font-size:7.5px">Presentation</div>
  <div class="a" style="left:19px;top:102px;font-size:18px;font-weight:800;line-height:1.1">Business</div>
  <div class="a" style="left:20px;top:123px;font-size:13px;font-weight:600">Marketing</div>
  <svg width="30" height="10"><circle cx="21" cy="163" r="1.6"/><circle cx="27" cy="163" r="1.6" fill="var(--green)"/><circle cx="33" cy="163" r="1.6"/></svg>
</section>

<section class="slide" style="left:697px;top:32px">
  <div class="title">Agenda</div><div class="rule" style="left:11px;top:26px"></div>
  <div class="brand"><i></i>Pellion Labs</div>
  <div class="a" style="left:32px;top:111px;width:113px;height:37px;border:5px solid var(--green);border-top:none"></div>
  <div class="photo" role="img" aria-label="Microscope and glassware on a lab bench" style="left:45px;top:41px;width:87px;height:95px"></div>
  <div class="a" style="left:160px;top:43px;width:130px">
    <div class="item-h">1. Lorem ipsum</div><div class="tiny" style="padding-left:8px">Lorem ipsum dolor sit amet, consectetuer adipiscing elit, sed diam nonummy nibh euismod tincid</div>
  </div>
  <div class="a" style="left:160px;top:73px;width:130px">
    <div class="item-h">2. Lorem ipsum</div><div class="tiny" style="padding-left:8px">Lorem ipsum dolor sit amet, consectetuer adipiscing elit, sed diam nonummy nibh euismod tincid</div>
  </div>
  <div class="a" style="left:160px;top:103px;width:130px">
    <div class="item-h">3. Lorem ipsum</div><div class="tiny" style="padding-left:8px">Lorem ipsum dolor sit amet, consectetuer adipiscing elit, sed diam nonummy nibh euismod tincid</div>
  </div>
  <div class="a" style="left:160px;top:131px;width:130px">
    <div class="item-h">4. Lorem ipsum</div><div class="tiny" style="padding-left:8px">Lorem ipsum dolor sit amet, consectetuer adipiscing elit, sed diam nonummy nibh euismod tincid</div>
  </div>
  <div class="pnum">2</div>
</section>

<!-- Row 2 -->
<section class="slide" style="left:34px;top:223px">
  <div class="title">Text Added Here</div><div class="rule" style="left:11px;top:26px"></div>
  <div class="brand"><i></i>Pellion Labs</div>
  <div class="a" style="left:25px;top:40px;width:132px">
    <div style="font-size:7px;font-weight:600">1. Text Added Here</div>
    <p class="tiny" style="text-align:justify">Lorem ipsum dolor sit amet, cons ectetuer adipiscing elit, sed diam nonummy nibh euismod tincidunt ut laoreet dolore magna aliquam erat volutpat. Ut wisi enim ad minim veniam, quis nostrud exerci tation ullamcorper suscipit lobortis nisl ut aliquip ex ea commodo consequat.</p>
    <p class="tiny" style="text-align:justify;margin-top:3px">Lorem ipsum dolor sit amet, consectetuer adipiscing elit, sed diam nonummy nibh euismod tincidunt ut laoreet dolore magna aliquam erat volutpat. Ut wisi enim ad minim veniam, quis nostrud exerci tation ullamcorper suscipit lobortis nisl ut aliquip ex ea commodo consequat.</p>
  </div>
  <div class="a" style="left:165px;top:40px;width:132px">
    <div style="font-size:7px;font-weight:600">2. Text Added Here</div>
    <p class="tiny" style="text-align:justify">Lorem ipsum dolor sit amet, cons ectetuer adipiscing elit, sed diam nonummy nibh euismod tincidunt ut laoreet dolore magna aliquam erat volutpat. Ut wisi enim ad minim veniam, quis nostrud exerci tation ullamcorper suscipit lobortis nisl ut aliquip ex ea commodo consequat.</p>
    <p class="tiny" style="text-align:justify;margin-top:3px">Lorem ipsum dolor sit amet, consectetuer adipiscing elit, sed diam nonummy nibh euismod tincidunt ut laoreet dolore magna aliquam erat volutpat. Ut wisi enim ad minim veniam, quis nostrud exerci tation ullamcorper suscipit lobortis nisl ut aliquip ex ea commodo consequat.</p>
  </div>
  <div class="num" style="left:28px;top:109px">1.</div>
  <div class="a" style="left:46px;top:107px"><div class="item-h">Lorem ipsum</div><div class="tiny">Lorem ipsum dolor sit amet, consectetuer adipiscing elit,<br>sed diam nonummy nibh euismod tincid</div></div>
  <div class="num" style="left:28px;top:137px">2.</div>
  <div class="a" style="left:46px;top:135px"><div class="item-h">Lorem ipsum</div><div class="tiny">Lorem ipsum dolor sit amet, consectetuer adipiscing elit,<br>sed diam nonummy nibh euismod tincid</div></div>
  <div class="num" style="left:168px;top:109px">1.</div>
  <div class="a" style="left:186px;top:107px"><div class="item-h">Lorem ipsum</div><div class="tiny">Lorem ipsum dolor sit amet, consectetuer adipiscing elit,<br>sed diam nonummy nibh euismod tincid</div></div>
  <div class="num" style="left:168px;top:137px">2.</div>
  <div class="a" style="left:186px;top:135px"><div class="item-h">Lorem ipsum</div><div class="tiny">Lorem ipsum dolor sit amet, consectetuer adipiscing elit,<br>sed diam nonummy nibh euismod tincid</div></div>
  <div class="footline"></div><div class="pnum">3</div>
</section>

<section class="slide" style="left:365px;top:223px">
  <div class="title" style="top:6px">Text Added Here</div><div class="rule" style="left:14px;top:22px"></div>
  <div class="brand"><i></i>Pellion Labs</div>
  <div class="a tiny" style="left:14px;top:29px;width:92px">
    <p>Lorem ipsum dolor sit amet, consectetuer adipiscing elit, sed diam nonummy nibh euismod tincidunt ut laoreet dolore magna aliquam erat volutpat. Ut wisi enim ad minim veniam</p>
    <p style="margin-top:3px">quis nostrud exerci tation ullamcorper suscipit lobortis nisl ut aliquip ex ea commo-do consequat. Duis autem vel eum iriure dolor in hendrerit.</p>
    <p style="margin-top:3px">quis nostrud exerci tation ullamcorper suscipit lobortis nisl ut aliquip ex ea commo-do consequat. Duis autem vel eum iriure dolor in hendrerit</p>
  </div>
  <div class="a" style="left:0;top:107px;width:104px;height:50px;background:var(--black)"></div>
  <div class="a" style="left:17px;top:111px;width:82px"><div style="font-size:4.6px;font-weight:600;color:var(--green)">Lorem ipsum</div><div class="tiny w" style="font-size:2.4px">Lorem ipsum dolor sit amet, consectetuer adipiscing elit, sed diam nonummy nibh euismod tincidunt ut laoreet</div></div>
  <div class="a" style="left:17px;top:133px;width:82px"><div style="font-size:4.6px;font-weight:600;color:var(--green)">Lorem ipsum</div><div class="tiny w" style="font-size:2.4px">Lorem ipsum dolor sit amet, consectetuer adipiscing elit, sed diam nonummy nibh euismod tincidunt ut laoreet</div></div>
  <svg width="321" height="180" font-family="Poppins, sans-serif">
    <circle cx="12" cy="115" r="2" fill="var(--green)"/><circle cx="12" cy="137" r="2" fill="var(--green)"/>
    <path d="M152 115 A55 55 0 1 0 145 90" fill="none" stroke="#000" stroke-width="2.5"/>
    <path d="M140 91 L145 98 L150 91" fill="none" stroke="#000" stroke-width="2.5"/>
    <circle cx="151" cy="110" r="2.5"/>
    <rect x="177" y="70" width="2" height="7"/><rect x="180" y="73" width="2" height="4"/><rect x="183" y="68" width="2" height="9"/><rect x="176" y="77" width="10" height="1"/>
    <text x="183" y="86" font-size="5" font-weight="600" text-anchor="middle">MAIN TITLE</text>
    <text x="183" y="90" font-size="2.2" fill="#8c8c8c" text-anchor="middle">Lorem ipsum dolor sit amet,</text>
    <text x="183" y="93" font-size="2.2" fill="#8c8c8c" text-anchor="middle">consectetuer adipiscing elit</text>
    <circle cx="242" cy="58" r="19" fill="var(--white)" stroke="var(--green)" stroke-width="4"/>
    <circle cx="242" cy="58" r="12" fill="var(--green)"/><circle cx="242" cy="58" r="7" fill="var(--white)"/>
    <circle cx="241" cy="57" r="2.5" fill="none" stroke="#000" stroke-width="1"/><path d="M239 59 L237 61" stroke="#000" stroke-width="1"/>
    <circle cx="254" cy="106" r="13" fill="var(--white)" stroke="var(--green)" stroke-width="3"/><circle cx="254" cy="106" r="6" fill="var(--green)"/><circle cx="254" cy="106" r="2.3"/>
    <circle cx="228" cy="140" r="10" fill="var(--white)" stroke="var(--green)" stroke-width="2.5"/><path d="M228 135 V144 M225 142 Q228 146 231 142" fill="none" stroke="#000" stroke-width="1"/>
    <circle cx="161" cy="128" r="9" fill="var(--white)" stroke="var(--green)" stroke-width="2.5"/><circle cx="161" cy="128" r="2.5"/>
    <g font-size="3" font-weight="600"><text x="269" y="43">85%</text><text x="225" y="95">80%</text><text x="186" y="126">50%</text><text x="252" y="150">75%</text></g>
    <path d="M261 44 L268 42 M269 110 L276 112 M171 127 L184 125 M238 146 L250 149" stroke="#000" stroke-width=".4"/>
    <g font-size="4.4" font-weight="600"><text x="274" y="52">Your Title</text><text x="281" y="97">Your Title</text><text x="268" y="137">Your Title</text><text x="121" y="125">Your Title</text></g>
    <g font-size="2" fill="#8c8c8c" text-anchor="end"><text x="298" y="56">Lorem ipsum dolor sit amet,</text><text x="298" y="59">consectetuer adipiscing elit,</text><text x="298" y="62">sed diam nonummy</text>
    <text x="304" y="101">Lorem ipsum dolor sit amet,</text><text x="304" y="104">consectetuer adipiscing elit,</text><text x="304" y="107">sed diam nonummy</text>
    <text x="292" y="141">Lorem ipsum dolor sit amet,</text><text x="292" y="144">consectetuer adipiscing elit,</text><text x="292" y="147">sed diam nonummy</text>
    <text x="144" y="129">Lorem ipsum dolor sit amet,</text><text x="144" y="132">consectetuer adipiscing</text><text x="144" y="135">sed diam nonummy</text></g>
  </svg>
  <div class="footline"></div><div class="pnum">4</div>
</section>

<section class="slide" style="left:697px;top:223px">
  <div class="title" style="left:15px;top:15px">About Us</div><div class="rule" style="left:15px;top:31px"></div>
  <div class="brand"><i></i>Pellion Labs</div>
  <div class="a tiny" style="left:15px;top:43px;width:165px">
    <p>Lorem ipsum dolor sit amet, consectetuer adipiscing elit, sed diam nonummy nibh euismod tincidunt ut laoreet dolore magna aliquam erat volutpat. Ut wisi enim ad minim veniam, quis nostrud exerci tation ullamcorper suscipit lobortis nisl ut aliquip.</p>
    <p style="margin-top:4px">Ex ea commodo consequat. Duis autem vel eum iriure dolor in hendrerit in vulputate velit esse molestie consequat, vel illum dolore eu feugiat nulla facilisis at vero eros et accumsan et iusto odio dignissim qui blandit praesent luptatum zzril delenit augue duis dolore te feugait nulla facilisi. Lorem ipsum dolor sit amet, cons ectetuer adipiscing elit, sed diam nonummy nibh euismod tincidunt ut laoreet dolore magna aliquam erat volutpat. Ut wisi enim ad minim veniam, quis nostrud exerci tation ullamcorper suscipit lobortis nisl ut aliquip ex ea commodo cons</p>
  </div>
  <svg width="321" height="180"><path d="M21 113 l3 2 l-3 2z" fill="var(--green)"/><path d="M97 113 l3 2 l-3 2z"/><path d="M21 131 l3 2 l-3 2z" fill="none" stroke="#000" stroke-width=".4"/><path d="M97 131 l3 2 l-3 2z" fill="none" stroke="var(--green)" stroke-width=".4"/></svg>
  <div class="a tiny" style="left:31px;top:112px;width:60px;font-size:2.6px">Lorem ipsum dolor sit amet, consectetuer adipiscing elit, sed diam nonummy nibh euismod</div>
  <div class="a tiny" style="left:107px;top:112px;width:60px;font-size:2.6px">Lorem ipsum dolor sit amet, consectetuer adipiscing elit, sed diam nonummy nibh euismod</div>
  <div class="a tiny" style="left:31px;top:130px;width:60px;font-size:2.6px">Lorem ipsum dolor sit amet, consectetuer adipiscing elit, sed diam nonummy nibh euismod</div>
  <div class="a tiny" style="left:107px;top:130px;width:60px;font-size:2.6px">Lorem ipsum dolor sit amet, consectetuer adipiscing elit, sed diam nonummy nibh euismod</div>
  <div class="a" style="left:186px;top:93px;width:113px;height:55px;border:4px solid var(--green);border-top:none"></div>
  <div class="photo" role="img" aria-label="Pressure gauge on calibration equipment" style="left:195px;top:36px;width:94px;height:104px;background:linear-gradient(140deg,#e2e4e6,#8d9196)"></div>
  <div class="footline"></div><div class="pnum">5</div>
</section>

<!-- Row 3 -->
<section class="slide" style="left:34px;top:415px">
  <div class="sq" style="left:0;top:0;width:93px;height:12px"></div>
  <div class="photo" role="img" aria-label="Technician in protective suit at process tanks" style="left:93px;top:0;width:60px;height:87px"></div>
  <div class="a" style="left:135px;top:45px;width:186px;height:97px;background:var(--black)"></div>
  <div class="photo" role="img" aria-label="Gloved hand holding a sample tube" style="left:162px;top:57px;width:63px;height:103px;background:linear-gradient(150deg,#e6eef5,#9fb8cc)"></div>
  <div class="brand"><i></i>Pellion Labs</div>
  <div class="a" style="left:16px;top:27px;font-size:10.5px;font-weight:600;line-height:1.35">Subject<br>Title</div>
  <div class="rule" style="left:16px;top:64px"></div>
  <div class="a tiny" style="left:16px;top:71px;width:72px;font-size:2.9px">Lorem ipsum dolor sit amet, consectetuer adipiscing elit, sed diam nonummy nibh euismod tincidunt ut laoreet dolore magna aliquam erat volutpat. Ut wisi enim ad minim veniam, quis nostrud exerci tation ullamcorper suscipit lobortis nisl ut aliquip ex ea commodo consequat. Duis autem vel eum iriure.</div>
  <div class="a" style="left:237px;top:58px;width:80px;font-size:8.5px;font-weight:600;line-height:1.3;color:var(--green)">Lorem Ipsum Dolor Sit Ametkeeper.</div>
  <div class="a tiny w" style="left:237px;top:100px;width:62px;font-size:3px">Lorem ipsum dolor sit amet, consectetuer adipisc-ing<br><br>elit, sed diam nonummy nibh euismod tincidunt ut laoreet dolore magna</div>
  <div class="pnum">6</div>
</section>

<section class="slide" style="left:365px;top:415px">
  <div class="sq" style="left:7px;top:8px;width:9px;height:9px"></div>
  <div class="brand"><i></i>Pellion Labs</div>
  <div class="a" style="left:25px;top:31px;font-size:13px;font-weight:600;line-height:1.5">Lorem Ipsum<br>Dolor Sit<br>Ametkeeper.</div>
  <div class="a tiny" style="left:26px;top:101px;width:100px">
    <p>Lorem ipsum dolor sit amet, consectetuer adipiscing elit, sed diam nonummy nibh euismod tincidunt erat volutpat.</p>
    <p style="margin-top:3px">Ut wisi enim ad minim veniam, quis nostrud exerci tation ullamcorper suscipit lobortis nisl ut aliquip ex ea commodo consequat. Ut wisi enim ad minim veniam, quis nostrud exerci tation ullamcorper suscipit lobortis nisl ut aliquip ex ea commodo consequat.</p>
  </div>
  <svg width="321" height="180">
    <rect x="143" y="38" width="23" height="23"/><rect x="143" y="78" width="23" height="23"/><rect x="143" y="121" width="23" height="23"/>
    <g fill="var(--green)"><circle cx="150" cy="46" r="2.3"/><circle cx="159" cy="46" r="2.3"/><circle cx="154.5" cy="44" r="2.6"/><path d="M146 55 q4-7 8.5 0 z M150 55 q4.5-8 9 0z M155 55 q4-7 8.5 0z"/>
    <circle cx="151" cy="83" r="2"/><circle cx="158" cy="83" r="2"/><rect x="149" y="86" width="4" height="9"/><rect x="156" y="86" width="4" height="9"/>
    <path d="M150 128 q4.5-4 4.5 1 q0-5 4.5-1 q0 4-4.5 7 q-4.5-3-4.5-7z"/><path d="M147 137 h5 l3 2 h6 v2 h-14z"/></g>
  </svg>
  <div class="a" style="left:177px;top:38px;width:130px"><div style="font-size:6.5px;font-weight:600">We Before Me</div><div class="tiny">ipsum dolor sit amet, cons ectetuer adipiscing elit, sed diam nonummy nibh euismod tincidunt ut laoreet</div></div>
  <div class="a" style="left:177px;top:78px;width:130px"><div style="font-size:6.5px;font-weight:600">We Are Good People</div><div class="tiny">ipsum dolor sit amet, cons ectetuer adipiscing elit, sed diam nonummy nibh euismod tincidunt ut laoreet dolore magna aliquam erat volutpat.</div></div>
  <div class="a" style="left:177px;top:122px;width:130px"><div style="font-size:6.5px;font-weight:600">We Work with Heart</div><div class="tiny">ipsum dolor sit amet, cons ectetuer adipiscing elit, sed diam nonummy nibh euismod tincidunt</div></div>
  <div class="pnum">7</div>
</section>

<section class="slide" style="left:697px;top:415px">
  <div class="title" style="top:11px">Text Added Here</div><div class="rule" style="left:11px;top:27px"></div>
  <div class="brand"><i></i>Pellion Labs</div>
  <div class="a" style="left:39px;top:44px;width:130px"><div style="font-size:5px;font-weight:600">01. <span style="margin-left:2px">Aliquam Erat Volutpat</span></div><div class="tiny" style="padding-left:12px;font-size:2.6px">Lorem ipsum dolor sit amet, consectetuer adipiscing elit, sed diam nonummy nibh euismod</div></div>
  <div class="a" style="left:39px;top:72px;width:130px"><div style="font-size:5px;font-weight:600">02. <span style="margin-left:2px">Consectetuer Adipiscing Elit</span></div><div class="tiny" style="padding-left:12px;font-size:2.6px">Lorem ipsum dolor sit amet, consectetuer adipiscing elit, sed diam nonummy nibh euismod tincidunt ut laoreet</div></div>
  <div class="a" style="left:39px;top:102px;width:130px"><div style="font-size:5px;font-weight:600">03. <span style="margin-left:2px">Duis Autem Vel Eum</span></div><div class="tiny" style="padding-left:12px;font-size:2.6px">Lorem ipsum dolor sit amet, consectetuer adipiscing elit, sed diam nonummy nibh euismod tincidunt.</div></div>
  <div class="a" style="left:39px;top:131px;width:130px"><div style="font-size:5px;font-weight:600">04. <span style="margin-left:2px">Aliquam Erat Volutpat</span></div><div class="tiny" style="padding-left:12px;font-size:2.6px">Lorem ipsum dolor sit amet, consectetuer adipiscing elit, sed diam nonummy nibh euismod tincidunt ut laoreet.</div></div>
  <div class="a" style="left:181px;top:43px;width:103px;height:107px;background:var(--black)"></div>
  <svg width="321" height="180">
    <g fill="var(--green)" stroke="var(--white)" stroke-width="1"><circle cx="182" cy="63" r="11"/><circle cx="182" cy="96" r="11"/><circle cx="182" cy="131" r="11"/></g>
    <rect x="177" y="59" width="10" height="7" fill="none" stroke="#000" stroke-width=".8"/><path d="M180 68 h4" stroke="#000" stroke-width=".8"/>
    <path d="M177 98 a3 3 0 0 1 2-5 a4 4 0 0 1 7 1 a2.5 2.5 0 0 1 0 4z M182 98 v4" fill="#000" stroke="#000" stroke-width=".6"/>
    <path d="M176 134 l4-5 l4 3 l4-5" fill="none" stroke="#000" stroke-width=".8"/><g fill="#000"><circle cx="176" cy="134" r="1.2"/><circle cx="180" cy="129" r="1.2"/><circle cx="184" cy="132" r="1.2"/><circle cx="188" cy="127" r="1.2"/></g>
  </svg>
  <div class="a" style="left:201px;top:55px;width:75px"><div style="font-size:6px;font-weight:600;color:var(--green)">Lorem ipsum</div><div class="tiny w" style="font-size:2.6px">ipsum dolor sit amet, cons ectetuer adipiscing elit, sed diam nonummy nibh euismod tincidunt ut laoreet</div></div>
  <div class="a" style="left:201px;top:88px;width:75px"><div style="font-size:6px;font-weight:600;color:var(--green)">Lorem ipsum</div><div class="tiny w" style="font-size:2.6px">ipsum dolor sit amet, cons ectetuer adipiscing elit, sed diam nonummy nibh euismod tincidunt ut laoreet</div></div>
  <div class="a" style="left:201px;top:123px;width:75px"><div style="font-size:6px;font-weight:600;color:var(--green)">Lorem ipsum</div><div class="tiny w" style="font-size:2.6px">ipsum dolor sit amet, cons ectetuer adipiscing elit, sed diam nonummy nibh euismod tincidunt</div></div>
  <div class="pnum">8</div>
</section>

<!-- Row 4 -->
<section class="slide" style="left:34px;top:607px">
  <div class="a" style="left:17px;top:12px;font-size:10.5px;font-weight:600;line-height:1.25">Market<br>Opportunities.</div>
  <div class="rule" style="left:17px;top:48px"></div>
  <div class="brand"><i></i>Pellion Labs</div>
  <div class="a" style="left:0;top:63px;width:111px;height:90px;background:var(--black)"></div>
  <div class="a" style="left:16px;top:68px;width:88px;font-size:4.6px;line-height:1.35;color:var(--white)">Lorem ipsum dolor sit amet, consectetuer adipiscing elit, sed diam nonummy nibh euismod tincidunt ut laoreet dolore magna aliquam erat volutpat. Ut wisi enim ad minim veniam, quis nostrud exerci tation ullamcorper suscipit lobortis nisl ut aliquip ex ea commodo consequat. Duis autem vel eum iriure dolor in hendrerit i</div>
  <div class="a" style="left:133px;top:19px;font-size:5.5px;font-weight:500">CONSECTETUER ADIPISCING</div>
  <svg width="321" height="180" font-family="Poppins, sans-serif">
    <g stroke="#bfbfbf" stroke-width=".4"><path d="M138 36 H297 M138 48.3 H297 M138 60.7 H297 M138 73 H297 M138 85.3 H297 M138 97.7 H297 M138 110 H297 M138 36 V110 M297 36 V110"/></g>
    <g font-size="5" fill="#333" text-anchor="end"><text x="136" y="38">60</text><text x="136" y="50">50</text><text x="136" y="62.5">40</text><text x="136" y="75">30</text><text x="136" y="87">20</text><text x="136" y="99.5">10</text><text x="136" y="112">0</text></g>
    <rect x="155" y="44.6" width="18" height="65.4" fill="var(--green)"/><rect x="188" y="70.5" width="18" height="39.5"/><rect x="222" y="52" width="18" height="58" fill="var(--green)"/><rect x="256" y="75.5" width="18" height="34.5"/>
    <g font-size="5" fill="#333" text-anchor="middle"><text x="164" y="119">JAN</text><text x="197" y="119">FEB</text><text x="231" y="119">MAR</text><text x="265" y="119">APR</text></g>
    <circle cx="134" cy="135" r="2" fill="var(--green)"/><circle cx="222" cy="135" r="2" fill="var(--green)"/>
  </svg>
  <div class="a" style="left:139px;top:132px;width:75px"><div style="font-size:5.8px;font-weight:600">Lorem Ipsum</div><div class="tiny">Lorem ipsum dolor sit amet, consectetuer adipiscing elit, sed diam nonummy nibh euismod tincidunt ut laoreet</div></div>
  <div class="a" style="left:228px;top:132px;width:75px"><div style="font-size:5.8px;font-weight:600">Lorem Ipsum</div><div class="tiny">Lorem ipsum dolor sit amet, consectetuer adipiscing elit, sed diam nonummy nibh euismod tincidunt ut laoreet</div></div>
  <div class="pnum">9</div>
</section>

<section class="slide" style="left:365px;top:607px">
  <div class="title" style="top:10px">Text Added Here</div><div class="rule" style="left:11px;top:26px"></div>
  <div class="brand"><i></i>Pellion Labs</div>
  <div class="a tiny" style="left:12px;top:34px;width:120px">Lorem ipsum dolor sit amet, consectetuer adipiscing elit, sed diam nonummy nibh euismod tincidunt ut laoreet dolore magna aliquam erat volutpat. Ut wisi enim ad minim veniam, quis nostrud exerci tation ullamcorper suscipit lobortis nisl ut aliquip ex ea commodo consequat. Duis</div>
  <svg width="321" height="180" font-family="Poppins, sans-serif">
    <g font-size="5" fill="#333" text-anchor="end"><text x="30" y="81">50%</text><text x="30" y="93">40%</text><text x="30" y="105">30%</text><text x="30" y="117">20%</text><text x="30" y="129">10%</text></g>
    <path d="M33 76 V141 H115" fill="none" stroke="#333" stroke-width=".8"/>
    <rect x="47" y="77" width="8" height="64" fill="var(--green)"/><rect x="65" y="100" width="8" height="41"/><rect x="84" y="129" width="8" height="12" fill="var(--green)"/><rect x="102" y="136" width="8" height="5"/>
    <g font-size="5" fill="#333" text-anchor="middle"><text x="51" y="151">1980</text><text x="69" y="151">1990</text><text x="88" y="151">2000</text><text x="106" y="151">2010</text></g>
    <g fill="none" stroke-width="3"><circle cx="219" cy="72" r="52" stroke="#efefef"/><circle cx="219" cy="72" r="44" stroke="#efefef"/><circle cx="219" cy="72" r="36" stroke="#efefef"/>
    <circle cx="219" cy="72" r="52" stroke="var(--green)" pathLength="100" stroke-dasharray="68 100" transform="rotate(-90 219 72)"/>
    <circle cx="219" cy="72" r="44" stroke="#000" pathLength="100" stroke-dasharray="45 100" transform="rotate(-90 219 72)"/>
    <circle cx="219" cy="72" r="36" stroke="var(--green)" pathLength="100" stroke-dasharray="35 100" transform="rotate(-90 219 72)"/></g>
    <text x="219" y="74" font-size="8" font-weight="600" text-anchor="middle">Add Text</text>
    <g font-size="4.2" font-weight="600"><text x="175" y="54">68%</text><text x="180" y="97">45%</text><text x="230" y="97">15%</text><text x="210" y="110">35%</text></g>
    <circle cx="152" cy="141" r="2" fill="var(--green)"/><circle cx="228" cy="141" r="2" fill="var(--green)"/>
  </svg>
  <div class="a" style="left:158px;top:138px;width:68px"><div style="font-size:5px;font-weight:600">Lorem ipsum</div><div class="tiny" style="font-size:2.4px">Lorem ipsum dolor sit amet, consectetuer adipiscing elit, sed diam nonummy nibh euismod tincidunt ut laoreet</div></div>
  <div class="a" style="left:234px;top:138px;width:68px"><div style="font-size:5px;font-weight:600">Lorem ipsum</div><div class="tiny" style="font-size:2.4px">Lorem ipsum dolor sit amet, consectetuer adipiscing elit, sed diam nonummy nibh euismod tincidunt ut laoreet</div></div>
  <div class="pnum">10</div>
</section>

<section class="slide" style="left:697px;top:607px">
  <div class="title" style="left:29px;top:13px">Text Added Here</div>
  <div class="brand"><i></i>Pellion Labs</div>
  <div class="sq" style="left:45px;top:32px;width:56px;height:3px"></div>
  <div class="photo" role="img" aria-label="Technician in protective gear working at a process line" style="left:19px;top:35px;width:107px;height:123px;background:linear-gradient(150deg,#dfe6ea,#8faab2)"></div>
  <svg width="321" height="180" font-family="Poppins, sans-serif">
    <g fill="var(--green)"><circle cx="152" cy="56" r="9"/><circle cx="152" cy="95" r="9"/><circle cx="152" cy="135" r="9"/></g>
    <g font-size="8" font-weight="700" text-anchor="middle"><text x="152" y="59">1</text><text x="152" y="98">2</text><text x="152" y="138">3</text></g>
  </svg>
  <div class="a tiny" style="left:168px;top:48px;width:116px;font-size:2.6px">Lorem ipsum dolor sit amet, consectetuer adipiscing elit, sed diam nonummy nibh euismod tincidunt ut laoreet dolore magna aliquam erat volutpat. Ut wisi enim ad minim veniam, quis nostrud exerci tation ullamcorper suscipit</div>
  <div class="a tiny" style="left:168px;top:86px;width:116px;font-size:2.6px">ullamcorper suscipit lobortis nisl ut aliquip ex ea commodo consequat. Duis autem vel eum iriure dolor in hendrerit in vulputate velit esse<br><br>molestie consequat, vel illum dolore eu feugiat nulla facilisis at vero eros et accumsan et iusto odio dignissim qui blandit praesent</div>
  <div class="a tiny" style="left:168px;top:128px;width:116px;font-size:2.6px">Lorem ipsum dolor sit amet, consectetuer adipiscing elit, sed diam nonummy nibh euismod tincidunt ut laoreet dolore magna aliquam erat volutpat. Ut wisi enim ad minim veniam, quis nostrud exerci tation ullamcorper suscipit</div>
  <div class="pnum">11</div>
</section>

<!-- Row 5 -->
<section class="slide" style="left:34px;top:798px">
  <div class="sq" style="left:7px;top:8px;width:7px;height:7px"></div>
  <div class="brand"><i></i>Pellion Labs</div>
  <div class="a" style="left:20px;top:32px;font-size:10px;font-weight:600;line-height:1.5">Creative Text<br>Heading Added<br>Here</div>
  <div class="num" style="left:22px;top:94px;width:10px;height:10px">1.</div>
  <div class="a" style="left:37px;top:93px;width:65px"><div style="font-size:4.6px;font-weight:600">Lorem ipsum</div><div class="tiny" style="font-size:2.3px">Lorem ipsum dolor sit amet, consectetuer adipiscing elit, sed diam nonummy nibh</div></div>
  <div class="num" style="left:22px;top:116px;width:10px;height:10px">2.</div>
  <div class="a" style="left:37px;top:115px;width:65px"><div style="font-size:4.6px;font-weight:600">Lorem ipsum</div><div class="tiny" style="font-size:2.3px">Lorem ipsum dolor sit amet, consectetuer adipiscing elit, sed diam nonummy nibh</div></div>
  <div class="num" style="left:22px;top:138px;width:10px;height:10px">3.</div>
  <div class="a" style="left:37px;top:137px;width:65px"><div style="font-size:4.6px;font-weight:600">Lorem ipsum</div><div class="tiny" style="font-size:2.3px">Lorem ipsum dolor sit amet, consectetuer adipiscing elit, sed diam nonummy nibh</div></div>
  <div class="photo" role="img" aria-label="Automated production line in a clean room" style="left:125px;top:33px;width:196px;height:75px;background:linear-gradient(160deg,#d4e5f3,#5d86ad)"></div>
  <div class="a tiny" style="left:125px;top:111px;width:185px;font-size:3.6px">
    <p>Lorem ipsum dolor sit amet, consectetuer adipiscing elit, sed diam nonummy nibh euismod tincidunt erat volutpat.</p>
    <p style="margin-top:3px">Ut wisi enim ad minim veniam, quis nostrud exerci tation ullamcorper suscipit lobortis nisl ut aliquip ex ea commodo consequat. Ut wisi enim ad minim veniam, quis nostrud exerci tation ullamcorper suscipit lobortis nisl ut aliquip ex ea commodo consequat.</p>
  </div>
  <div class="pnum">12</div>
</section>

<section class="slide" style="left:365px;top:798px">
  <div class="title" style="top:12px">Text Added Here</div><div class="rule" style="left:11px;top:28px"></div>
  <div class="brand"><i></i>Pellion Labs</div>
  <svg width="321" height="180">
    <g stroke="#000" stroke-width=".6"><rect x="57" y="40" width="24" height="24" fill="var(--green)"/><rect x="149" y="40" width="24" height="24"/><rect x="241" y="40" width="24" height="24" fill="var(--green)"/>
    <rect x="57" y="105" width="24" height="24"/><rect x="149" y="105" width="24" height="24" fill="var(--green)"/><rect x="241" y="105" width="24" height="24"/></g>
    <g fill="none" stroke-width=".8">
      <g stroke="#000"><circle cx="66" cy="49" r="2"/><circle cx="72" cy="49" r="2"/><path d="M62 57 q4-6 8 0 M68 57 q4-6 8 0"/></g>
      <g stroke="var(--green)"><circle cx="158" cy="50" r="3"/><circle cx="164" cy="48" r="2.5"/><path d="M157 57 h8 v3 h-8z"/></g>
      <g stroke="#000"><path d="M246 58 v-4 h3 v4 M251 58 v-6 h3 v6 M256 58 v-8 h3 v8 M246 49 l10-4 l4 1"/></g>
      <g stroke="var(--green)"><path d="M63 111 v10 h12 M64 114 q3 5 10 6 l-2-3"/></g>
      <g stroke="#000"><path d="M157 113 h8 l2 3 q2 8-6 9 q-8-1-6-9z M161 116 v6"/></g>
      <g stroke="var(--green)"><path d="M253 109 l3 3 h4 v4 l3 3 l-3 3 v4 h-4 l-3 3 l-3-3 h-4 v-4 l-3-3 l3-3 v-4 h4z"/></g>
    </g>
  </svg>
  <div class="a" style="left:34px;top:68px;width:70px;text-align:center"><div style="font-size:5.5px;font-weight:600">Lorem ipsum</div><div class="tiny" style="font-size:2.5px">Lorem ipsum dolor sit amet, consectetuer adipiscing elit, sed diam nonummy nibh euismod tincidunt ut laoreet</div></div>
  <div class="a" style="left:126px;top:68px;width:70px;text-align:center"><div style="font-size:5.5px;font-weight:600">Lorem ipsum</div><div class="tiny" style="font-size:2.5px">Lorem ipsum dolor sit amet, consectetuer adipiscing elit, sed diam nonummy nibh euismod tincidunt ut laoreet</div></div>
  <div class="a" style="left:218px;top:68px;width:70px;text-align:center"><div style="font-size:5.5px;font-weight:600">Lorem ipsum</div><div class="tiny" style="font-size:2.5px">Lorem ipsum dolor sit amet, consectetuer adipiscing elit, sed diam nonummy nibh euismod tincidunt ut laoreet</div></div>
  <div class="a" style="left:34px;top:133px;width:70px;text-align:center"><div style="font-size:5.5px;font-weight:600">Lorem ipsum</div><div class="tiny" style="font-size:2.5px">Lorem ipsum dolor sit amet, consectetuer adipiscing elit, sed diam nonummy nibh euismod tincidunt ut laoreet</div></div>
  <div class="a" style="left:126px;top:133px;width:70px;text-align:center"><div style="font-size:5.5px;font-weight:600">Lorem ipsum</div><div class="tiny" style="font-size:2.5px">Lorem ipsum dolor sit amet, consectetuer adipiscing elit, sed diam nonummy nibh euismod tincidunt ut laoreet</div></div>
  <div class="a" style="left:218px;top:133px;width:70px;text-align:center"><div style="font-size:5.5px;font-weight:600">Lorem ipsum</div><div class="tiny" style="font-size:2.5px">Lorem ipsum dolor sit amet, consectetuer adipiscing elit, sed diam nonummy nibh euismod tincidunt ut laoreet</div></div>
  <div class="pnum">13</div>
</section>

<section class="slide" style="left:697px;top:798px">
  <div class="title" style="top:8px">Our Timemap</div><div class="rule" style="left:11px;top:24px"></div>
  <div class="brand"><i></i>Pellion Labs</div>
  <svg width="321" height="180" font-family="Poppins, sans-serif">
    <path d="M61 34 V118 H276" stroke="#8c8c8c" stroke-width=".6" fill="none"/><circle cx="61" cy="34" r="1.3" fill="#8c8c8c"/>
    <g fill="#8c8c8c"><circle cx="61" cy="118" r="1.3"/><circle cx="82.5" cy="118" r="1.3"/><circle cx="104" cy="118" r="1.3"/><circle cx="125.5" cy="118" r="1.3"/><circle cx="147" cy="118" r="1.3"/><circle cx="168.5" cy="118" r="1.3"/><circle cx="190" cy="118" r="1.3"/><circle cx="211.5" cy="118" r="1.3"/><circle cx="233" cy="118" r="1.3"/><circle cx="254.5" cy="118" r="1.3"/><circle cx="276" cy="118" r="1.3"/></g>
    <g font-size="4.6" fill="#333" text-anchor="middle"><text x="61" y="127">0%</text><text x="82.5" y="127">10%</text><text x="104" y="127">20%</text><text x="125.5" y="127">30%</text><text x="147" y="127">40%</text><text x="168.5" y="127">50%</text><text x="190" y="127">60%</text><text x="211.5" y="127">70%</text><text x="233" y="127">80%</text><text x="254.5" y="127">90%</text><text x="276" y="127">100%</text></g>
    <rect x="61" y="43" width="31" height="17" fill="var(--green)"/><rect x="92" y="43" width="44" height="17"/><rect x="136" y="43" width="31" height="17" fill="var(--green)"/><rect x="167" y="43" width="109" height="17"/>
    <rect x="61" y="67" width="76" height="17"/><rect x="137" y="67" width="53" height="17" fill="var(--green)"/><rect x="190" y="67" width="44" height="17"/><rect x="234" y="67" width="42" height="17" fill="var(--green)"/>
    <rect x="61" y="93" width="44" height="17"/><rect x="105" y="93" width="63" height="17" fill="var(--green)"/><rect x="168" y="93" width="22" height="17"/><rect x="190" y="93" width="86" height="17" fill="var(--green)"/>
    <g font-size="5" text-anchor="middle"><g fill="#fff"><text x="114" y="53.5">40%</text><text x="221" y="53.5">90%</text><text x="99" y="77.5">50%</text><text x="212" y="77.5">20%</text><text x="83" y="103.5">30%</text><text x="179" y="103.5">10%</text></g>
    <g fill="#eaff80"><text x="76.5" y="53.5">20%</text><text x="151.5" y="53.5">10%</text><text x="163.5" y="77.5">30%</text><text x="255" y="77.5">20%</text><text x="136.5" y="103.5">60%</text><text x="233" y="103.5">70%</text></g></g>
    <g font-size="6" font-weight="600"><text x="41" y="53.5">2019</text><text x="41" y="77.5">2020</text><text x="41" y="103.5">2021</text></g>
    <g fill="var(--green)"><circle cx="33" cy="51" r="2.5"/><rect x="32" y="53" width="2" height="2.5"/><path d="M33 71 v6 M30 75 q3 4 6 0" stroke="var(--green)" stroke-width="1" fill="none"/><circle cx="33" cy="101" r="3"/><rect x="32" y="96" width="2" height="2"/></g>
  </svg>
  <div class="a" style="left:57px;top:136px;width:50px"><div style="font-size:5px;font-weight:600">Lorem Ipsum</div><div class="tiny" style="font-size:2.3px">Lorem ipsum dolor sit amet, consectetuer adipiscing elit, sed diam nonummy nibh euismod tincid</div></div>
  <div class="a" style="left:115px;top:136px;width:50px"><div style="font-size:5px;font-weight:600">Lorem Ipsum</div><div class="tiny" style="font-size:2.3px">Lorem ipsum dolor sit amet, consectetuer adipiscing elit, sed diam nonummy nibh euismod tincid</div></div>
  <div class="a" style="left:176px;top:136px;width:50px"><div style="font-size:5px;font-weight:600">Lorem Ipsum</div><div class="tiny" style="font-size:2.3px">Lorem ipsum dolor sit amet, consectetuer adipiscing elit, sed diam nonummy nibh euismod tincid</div></div>
  <div class="a" style="left:238px;top:136px;width:50px"><div style="font-size:5px;font-weight:600">Lorem Ipsum</div><div class="tiny" style="font-size:2.3px">Lorem ipsum dolor sit amet, consectetuer adipiscing elit, sed diam nonummy nibh euismod tincid</div></div>
  <div class="pnum">14</div>
</section>

<!-- Row 6 -->
<section class="slide" style="left:34px;top:989px">
  <div class="title" style="left:13px;top:9px">Text Added Here</div><div class="rule" style="left:13px;top:25px"></div>
  <div class="brand"><i></i>Pellion Labs</div>
  <div class="a tiny" style="left:13px;top:34px;width:102px">
    <p>Lorem ipsum dolor sit amet, consectetuer adipisc-ing elit, sed diam nonummy nibh euismod tincidunt ut laoreet dolore magna aliquam erat volutpat. Ut wisi enim ad minim veniam,</p>
    <p style="margin-top:3px">quis nostrud exerci tation ullamcorper suscipit lobortis nisl ut aliquip ex ea commodo consequat. Duis autem vel eum iriure dolor in hendrerit in vulputate velit esse</p>
    <p style="margin-top:3px">Lorem ipsum dolor sit amet, consectetuer adipisc-ing elit, sed diam nonummy nibh euismod tincidunt ut laoreet dolore magna aliquam erat</p>
  </div>
  <div class="num" style="left:20px;top:104px;width:9px;height:9px;font-size:5px">1.</div>
  <div class="a" style="left:32px;top:104px;width:80px"><div style="font-size:4.2px;font-weight:600">Lorem ipsum</div><div class="tiny" style="font-size:2.3px">Lorem ipsum dolor sit amet, consectetuer adipiscing elit, sed diam nonummy nibh euismod</div></div>
  <div class="num" style="left:20px;top:124px;width:9px;height:9px;font-size:5px">2.</div>
  <div class="a" style="left:32px;top:124px;width:80px"><div style="font-size:4.2px;font-weight:600">Lorem ipsum</div><div class="tiny" style="font-size:2.3px">Lorem ipsum dolor sit amet, consectetuer adipiscing elit, sed diam nonummy nibh euismod</div></div>
  <div class="num" style="left:20px;top:144px;width:9px;height:9px;font-size:5px">3.</div>
  <div class="a" style="left:32px;top:144px;width:80px"><div style="font-size:4.2px;font-weight:600">Lorem ipsum</div><div class="tiny" style="font-size:2.3px">Lorem ipsum dolor sit amet, consectetuer adipiscing elit, sed diam nonummy nibh euismod</div></div>
  <svg width="321" height="180">
    <g fill="#fff" stroke="#000" stroke-width="1.3"><rect x="148" y="25" width="37" height="77" rx="3"/><rect x="196" y="49" width="37" height="76" rx="3"/><rect x="243" y="76" width="39" height="76" rx="3"/></g>
    <g fill="#000"><rect x="162" y="27" width="9" height="1.5" rx=".7"/><rect x="210" y="51" width="9" height="1.5" rx=".7"/><rect x="258" y="78" width="9" height="1.5" rx=".7"/></g>
    <g fill="none" stroke="var(--green)" stroke-width=".8"><rect x="162" y="67" width="8" height="5"/><rect x="211" y="101" width="6" height="5"/><circle cx="262" cy="121" r="3"/></g>
  </svg>
  <div class="a" style="left:152px;top:35px;font-size:4.3px;line-height:1.3">Lorem<br>ipsum dolor</div>
  <div class="a tiny" style="left:152px;top:48px;width:28px;font-size:1.9px;color:#555">To introduce the students to the changing landscape of marketing and equip them with knowledge and tools to navigate the digital marketing world.</div>
  <div class="a" style="left:200px;top:59px;font-size:4.3px;line-height:1.3">Dolor sit<br>amet, conse</div>
  <div class="a tiny" style="left:200px;top:109px;width:28px;font-size:1.9px;color:#555">You will learn concepts and ideas in digital marketing as well as how to use different tools and strategies.</div>
  <div class="a" style="left:248px;top:87px;font-size:4.3px">Consec</div>
  <div class="a" style="left:248px;top:94px;font-size:3px;letter-spacing:.8px">• • • • • •</div>
  <div class="a tiny" style="left:248px;top:128px;width:29px;font-size:1.9px;color:#555">You are required to pass 80% of the evaluation test to obtain the certificate. The test can only be taken 3 times.</div>
  <div class="pnum">15</div>
</section>

<section class="slide" style="left:365px;top:989px">
  <div class="title" style="left:11px;top:8px">Our Team</div><div class="rule" style="left:11px;top:24px"></div>
  <div class="brand"><i></i>Pellion Labs</div>
  <div class="a tiny" style="left:11px;top:31px;width:300px;font-size:2.9px">
    <p>Lorem ipsum dolor sit amet, consectetuer adipiscing elit, sed diam nonummy nibh euismod tincidunt ut laoreet dolore magna aliquam erat volutpat. Ut wisi enim ad minim veniam, quis nostrud exerci tation ullamcorper suscipit lobortis nisl ut aliquip ex ea commodo consequat. Duis autem vel eum iriure dolor in hendrerit in vulputate velit esse molestie consequat, vel illum dolore eu feugiat nulla facilisis at vero eros et accumsan et iusto odio dignissim qui blandit praesent luptatum zzril delenit augue duis dolore te feugait nulla facilisi.</p>
    <p style="margin-top:3px">Lorem ipsum dolor sit amet, cons ectetuer adipiscing elit, sed diam nonummy nibh euismod tincidunt ut laoreet dolore magna aliquam erat volutpat. Ut wisi enim ad minim veniam, quis nostrud exerci tation ullamcorper suscipit lobortis nisl ut aliquip ex ea commodo.</p>
  </div>
  <svg width="321" height="180">
    <g fill="var(--green)"><rect x="28" y="83" width="47" height="20"/><rect x="98" y="83" width="47" height="20"/><rect x="170" y="83" width="47" height="20"/><rect x="243" y="83" width="47" height="20"/></g>
    <g fill="#d0d3d6" stroke="#fff" stroke-width="1.2"><circle cx="52" cy="103" r="13"/><circle cx="122" cy="103" r="13"/><circle cx="194" cy="103" r="13"/><circle cx="267" cy="103" r="13"/></g>
  </svg>
  <div class="a" style="left:22px;top:120px;width:60px;text-align:center"><div style="font-size:5.5px;font-weight:600">DANA REYES</div><div class="tiny" style="font-size:2.2px">ipsum dolor sit amet, cons ectetuer adipiscing elit, sed diam nonummy nibh euismod tincidunt<br><br>ut laoreet dolore magna aliquam erat volutpat. Ut wisi enim ad minim veniam, quis nostrud</div></div>
  <div class="a" style="left:92px;top:120px;width:60px;text-align:center"><div style="font-size:5.5px;font-weight:600">MARA LIND</div><div class="tiny" style="font-size:2.2px">ipsum dolor sit amet, cons ectetuer adipiscing elit, sed diam nonummy nibh euismod tincidunt ut laoreet<br><br>aliquam erat volutpat. Ut wisi enim ad minim veniam, quis nostrud</div></div>
  <div class="a" style="left:164px;top:120px;width:60px;text-align:center"><div style="font-size:5.5px;font-weight:600">DANA REYES</div><div class="tiny" style="font-size:2.2px">ipsum dolor sit amet, cons ectetuer adipiscing elit, sed diam nonummy nibh euismod tincidunt ut laoreet dolore magna aliquam erat volutpat.<br><br>Ut wisi enim ad minim veniam, quis nostrud</div></div>
  <div class="a" style="left:237px;top:120px;width:60px;text-align:center"><div style="font-size:5.5px;font-weight:600">MARA LIND</div><div class="tiny" style="font-size:2.2px">ipsum dolor sit amet, cons ectetuer adipiscing elit,<br><br>sed diam nonummy nibh euismod tincidunt ut laoreet dolore magna<br><br>aliquam erat volutpat. Ut wisi enim ad minim veniam</div></div>
  <div class="pnum">16</div>
</section>

<section class="slide" style="left:697px;top:989px">
  <div class="logo" style="left:94px;top:24px;font-size:13px;gap:7px"><i style="width:28px;height:28px"></i>Pellion Labs</div>
  <div class="a" style="left:20px;top:76px;width:122px;text-align:right;font-size:28px;font-weight:700;line-height:1.05">Thank<br>You</div>
  <div class="photo" role="img" aria-label="Scientist working with pipettes at a lab bench" style="left:147px;top:72px;width:107px;height:82px;background:linear-gradient(140deg,#e8eef3,#9db1c2)"></div>
  <div class="sq" style="left:257px;top:72px;width:15px;height:82px"></div>
  <div class="a" style="left:257px;top:72px;width:15px;height:82px;display:flex;align-items:center;justify-content:center">
    <div style="transform:rotate(-90deg);white-space:nowrap;font-size:5px;font-weight:500;letter-spacing:1px">www.pellionlabs.com</div>
  </div>
  <div class="sq" style="left:10px;top:161px;width:9px;height:9px"></div>
</section>

</body>
</html>
```